Postcard needed for expert witness service

Looking for a professional postcard that will be mailed to personal injury lawyers / law firms to introduce my expert witness services.

Target Market(s)

Law firms, personal injury lawyers

Industry/Entity Type

Expert witness, law

Font styles to use
Sans Serif

Requirements
Must have
• Logo: The Frost Counsel [Main Heading]Do you handle snow and ice related slip and falls? Darrel is one of the top snow industry experts in the country! [Following should be in a list type fashion, possibly bulleted]Darrel's credentials: Accredited Winter Practitioner (AWP), past WRTA board member and chair, former ISO 9001 certified snow company owner , 32 years in the industry. (555) 284-3917 NOTES: Postcard will be 4" x 6" Please use both sides however must have room for labels and stamp
Should not have
• Wouldn't suggest using both photos on same side. Honestly, feel free to only use one of the slip and fall photos if it works out better. Thanks!

```html
<!DOCTYPE html>
<html lang="en">
<head>
<meta charset="utf-8">
<title>The Frost Counsel – Postcard</title>
<link href="https://fonts.googleapis.com/css2?family=Montserrat:wght@500&family=Poppins:wght@400;600;700;800&display=swap" rel="stylesheet">
<style>
  :root{
    --stage:#5f5f5f;
    --ink:#000000;
    --paper:#ffffff;
    --accent:#8fd4ec;
    --steel:#9aa3a8;
    --rule:#b8bcbf;
  }
  *{box-sizing:border-box;margin:0;padding:0}
  html,body{width:1200px;height:1200px;overflow:hidden;background:var(--stage)}
  body{position:relative;font-family:"Poppins",sans-serif;color:var(--paper)}
  .card{position:absolute;overflow:hidden}
  .card-front{left:81px;top:82px;width:735px;height:491px}
  .card-back{left:376px;top:630px;width:747px;height:498px;background:var(--paper)}
  .layer{position:absolute;left:0;top:0;width:100%;height:100%}

  .brand-name{position:absolute;font-family:"Poppins",sans-serif;font-weight:600;font-size:24px;line-height:1;white-space:nowrap}
  .brand-front{left:43px;top:44px;color:var(--ink)}
  .brand-back{left:42px;top:180px;color:var(--paper)}

  .headline{position:absolute;left:36px;top:156px;font-weight:700;line-height:1}
  .headline .h-lead{display:block;font-size:24px}
  .headline .h-mid{display:block;font-size:19px;margin-top:8px}
  .headline .h-key{display:block;font-size:36px;color:var(--accent);margin-top:6px;letter-spacing:-.3px}
  .intro{position:absolute;left:36px;top:266px;font-family:"Montserrat",sans-serif;font-size:12px;line-height:15px;font-weight:500}
  .intro b{font-size:17px;font-weight:500}
  .intro-rule{position:absolute;left:38px;top:310px;width:47px;height:2px;background:var(--paper)}
  .phone-front{position:absolute;left:530px;top:413px;font-size:25px;font-weight:700;letter-spacing:.3px}

  .creds-title{position:absolute;left:40px;top:244px;font-size:22px;font-weight:800;color:var(--accent);white-space:nowrap}
  .creds-title-rule{position:absolute;left:289px;top:263px;width:102px;height:1px;background:var(--rule)}
  .cred{position:absolute;display:flex;gap:11px;font-size:15px;line-height:18px;font-weight:400;width:180px}
  .cred svg{flex:none;margin-top:1px}
  .phone-back{position:absolute;left:40px;top:425px;display:flex;align-items:center;gap:6px;font-size:26px;font-weight:700}
  .stamp-box{position:absolute;left:624px;top:21px;width:78px;height:90px;border:1.5px solid var(--rule)}
  .address-line{position:absolute;left:504px;width:220px;height:1px;background:var(--rule)}
</style>
</head>
<body>

<!-- Front -->
<section class="card card-front">
  <svg class="layer" viewBox="0 0 735 491" role="img" aria-label="Photo of a man slipping and falling on an icy city sidewalk, a backpack lying on the ground">
    <defs>
      <linearGradient id="sceneSky" x1="0" y1="0" x2="1" y2="0">
        <stop offset="0" stop-color="#f6f6f6"/>
        <stop offset=".6" stop-color="#e9eaec"/>
        <stop offset="1" stop-color="#6a7a93"/>
      </linearGradient>
      <linearGradient id="sceneGround" x1="0" y1="0" x2="0" y2="1">
        <stop offset="0" stop-color="#8d8f92"/>
        <stop offset="1" stop-color="#c9cbcd"/>
      </linearGradient>
      <radialGradient id="sceneFigure" cx=".72" cy=".45" r=".32">
        <stop offset="0" stop-color="#3c5a86"/>
        <stop offset="1" stop-color="#3c5a86" stop-opacity="0"/>
      </radialGradient>
    </defs>
    <rect width="735" height="491" fill="url(#sceneSky)"/>
    <rect width="735" height="491" fill="url(#sceneFigure)"/>
    <rect y="380" width="735" height="111" fill="url(#sceneGround)"/>
  </svg>
  <svg class="layer" viewBox="0 0 735 491" aria-hidden="true">
    <polygon points="0,95 88,112 0,119" fill="var(--steel)"/>
    <polygon points="0,126 206,102 420,330 420,380 0,380" fill="var(--ink)"/>
    <polygon points="470,406 735,406 735,454 513,454" fill="var(--ink)"/>
  </svg>

  <div class="brand-name brand-front">The Frost Counsel</div>

  <h1 class="headline">
    <span class="h-lead">Do you handle</span>
    <span class="h-mid">Snow and ice related</span>
    <span class="h-key">Slip and Falls?</span>
  </h1>
  <p class="intro"><b>Darrel</b> is one of the top snow industry<br>experts in the country!</p>
  <div class="intro-rule"></div>
  <div class="phone-front">(555) 284-3917</div>
</section>

<!-- Back -->
<section class="card card-back">
  <svg class="layer" viewBox="0 0 747 498" aria-hidden="true">
    <polygon points="0,0 202,0 430,267 430,498 0,498" fill="var(--ink)"/>
    <polygon points="212,0 253,0 367,185" fill="var(--steel)"/>
  </svg>

  <div class="brand-name brand-back">The Frost Counsel</div>

  <h2 class="creds-title">Darrel's Credentials</h2>
  <div class="creds-title-rule"></div>

  <div class="cred" style="left:40px;top:286px">
    <svg width="20" height="22" viewBox="0 0 20 22"><polygon points="10,1 19,6 19,16 10,21 1,16 1,6" fill="none" stroke="#fff" stroke-width="1.6"/><path d="M6 11l3 3 5-6" fill="none" stroke="#fff" stroke-width="1.8"/></svg>
    <span>Accredited Winter Practitioner (AWP)</span>
  </div>
  <div class="cred" style="left:40px;top:336px">
    <svg width="20" height="22" viewBox="0 0 20 22"><polygon points="10,1 19,6 19,16 10,21 1,16 1,6" fill="none" stroke="#fff" stroke-width="1.6"/><path d="M6 11l3 3 5-6" fill="none" stroke="#fff" stroke-width="1.8"/></svg>
    <span>Former ISO 9001 certified snow company owner</span>
  </div>
  <div class="cred" style="left:229px;top:286px">
    <svg width="20" height="22" viewBox="0 0 20 22"><polygon points="10,1 19,6 19,16 10,21 1,16 1,6" fill="none" stroke="#fff" stroke-width="1.6"/><path d="M6 11l3 3 5-6" fill="none" stroke="#fff" stroke-width="1.8"/></svg>
    <span>Past WRTA board member and chair</span>
  </div>
  <div class="cred" style="left:229px;top:333px">
    <svg width="20" height="22" viewBox="0 0 20 22"><polygon points="10,1 19,6 19,16 10,21 1,16 1,6" fill="none" stroke="#fff" stroke-width="1.6"/><path d="M6 11l3 3 5-6" fill="none" stroke="#fff" stroke-width="1.8"/></svg>
    <span>32 years in the industry</span>
  </div>

  <div class="phone-back">
    <svg width="32" height="32" viewBox="0 0 32 32"><circle cx="16" cy="16" r="14.5" fill="none" stroke="#fff" stroke-width="2"/><path d="M11 8c-1.5 1-2.5 2.5-2 5 1 5 5 9.5 10 11 2.5.7 4-.5 5-2l-3-3-2.5 1.5c-2-1-4-3-5-5l1.5-2.5z" fill="none" stroke="#fff" stroke-width="1.8" stroke-linejoin="round"/></svg>
    <span>(555) 284-3917</span>
  </div>

  <div class="stamp-box"></div>
  <div class="address-line" style="top:192px"></div>
  <div class="address-line" style="top:252px"></div>
  <div class="address-line" style="top:312px"></div>
  <div class="address-line" style="top:372px"></div>
  <div class="address-line" style="top:432px"></div>
</section>

</body>
</html>
```